Labels for essential oils small botlles

We are Slovenia based company Velnira Botanic Ltd. www.velnira-botanic.com We offer essential oils as pure essential oils or blends (mixed) essential oils. We have different kind of essential oils 40+ and blends. We sell in different sizes as: 10ml, 30ml, 50ml and 100ml. But majority is 10ml.
All essential oils are in glass bottles with closer. We will now change bottles style from amber to cobalt blue with black closure (see picture attached)
We would like to have different stile of label for different category of essential oils. Here is link about different categories of essential oils https://www.vialquarry.com/mixing-guides/ . The different style / color could be by note:
- Top notes
- Middle notes
- Base notes
- Mixes – different oils mixed together and named as chill out, deep breath, sleep well, etc
Possible is also differentiation regarding:
• Citrus
• Floral
• Herbaceous
• Camphoraceous
• Spicy
• Resinous
• Woody
• Earthy
• Mixes

On labels should be also pictograms according to REACH directive of EU and label according to CPL (see attached file). We would also like to add EAN code attached on the edge of the label. On label is some text fixed I try to show in pdf attached file and some is variable depends from essential oil and date of production.

Meaning we need general labels for each note or other classification and one for mixes – you could also show your option or classification on something else with story behind.

10 ml roll 30 mm x 70 mm (1,25”x3”) but finial dimensions will follow.

We use Tessaro Qm700 printer. For editing labels we use BarTender which support also EAN codes. We import labels as picture in background or different according to your instructions.

Target Market(s)

Retail, health and wellness, all audiences and web shop

Industry/Entity Type

Health And Wellness

Font styles to use
Other font styles liked:
• GillLigHr is our font but could be different

Colors

Designer to choose colors to be used in the design.

Requirements
Must have
• Label should be as template that we could use for different oils in same group. More in attached document. According to CLP we have to put red pictograms on labels which is not nice and should be some how nicely integrated. on the edge EAB dar code that products could be sell through online.
Nice to have
• Different colours, some symbol as a drop or flower or herb. Logo is not necessary that is on label. We would like that label it self represent our brand.

```html
<!DOCTYPE html>
<html lang="en">
<head>
<meta charset="utf-8">
<title>Velnira Essential Oil Label</title>
<link href="https://fonts.googleapis.com/css2?family=Quicksand:wght@400;500;600&family=Oswald:wght@300&display=swap" rel="stylesheet">
<style>
  :root {
    --page: #f3f3f3;
    --label: #ffffff;
    --ink: #3f3f3f;
    --tab: #6b6b68;
    --tab-text: #ffffff;
    --band: #c9f27a;
    --sprig-light: #f6f6f5;
    --sprig-dark: #dcdcda;
  }
  * { margin: 0; padding: 0; box-sizing: border-box; }
  html, body { width: 900px; height: 1200px; overflow: hidden; background: var(--page); }
  .canvas { position: relative; width: 900px; height: 1200px; }
  .label {
    position: absolute; left: 116px; top: 100px;
    width: 667px; height: 1000px;
    background: var(--label);
    box-shadow: 0 2px 10px rgba(0,0,0,0.08);
    color: var(--ink);
    font-family: "Quicksand", sans-serif;
    overflow: hidden;
  }
  .brand-tab {
    position: absolute; left: 57px; top: 12px; width: 64px; height: 285px;
    background: var(--tab); border-radius: 0 0 10px 10px;
    display: flex; align-items: center; justify-content: center;
  }
  .brand-tab span {
    transform: rotate(-90deg);
    color: var(--tab-text); font-size: 42px; font-weight: 500; white-space: nowrap;
  }
  .sprig-art {
    position: absolute; left: 470px; top: 12px; width: 197px; height: 360px;
    background: linear-gradient(170deg, var(--sprig-dark), var(--sprig-light) 75%, var(--label));
    border-radius: 0 0 0 90px;
  }
  .brand-name {
    position: absolute; left: 40px; right: 40px; top: 378px;
    text-align: center; font-size: 150px; font-weight: 400; line-height: 1;
    letter-spacing: 2px;
  }
  .product-type {
    position: absolute; left: 57px; right: 74px; top: 548px;
    display: flex; align-items: center; gap: 16px;
    font-family: "Oswald", sans-serif; font-weight: 300;
    font-size: 54px; letter-spacing: 2px; line-height: 1;
  }
  .product-type .rule { flex: 1; height: 4px; background: var(--ink); }
  .oil-band {
    position: absolute; left: 30px; width: 580px; top: 700px; height: 112px;
    background: var(--band);
    display: flex; align-items: center; padding: 0 18px;
    font-weight: 500; font-size: 36px; line-height: 1.05;
  }
  .botanical-name .genus { text-transform: uppercase; display: block; }
  .band-divider { width: 3px; height: 84px; background: var(--ink); margin: 0 16px; }
  .organic-claim { font-size: 34px; }
  .volume {
    position: absolute; left: 0; right: 0; top: 870px;
    text-align: center; font-size: 42px; font-weight: 500;
  }
</style>
</head>
<body>
  <main class="canvas">
    <section class="label">
      <div class="brand-tab"><span>velnira</span></div>
      <div class="sprig-art" role="img" aria-label="Line drawing of a flowering herb sprig"></div>
      <h1 class="brand-name">velnira</h1>
      <div class="product-type"><span class="rule"></span><span>ESSENTIAL OIL</span><span class="rule"></span></div>
      <div class="oil-band">
        <div class="botanical-name"><span class="genus">Cymbopogon</span><span>winterianus</span></div>
        <div class="band-divider"></div>
        <div class="organic-claim">100%<br>Organic</div>
      </div>
      <p class="volume">10ml</p>
    </section>
  </main>
</body>
</html>
```